Geschäftspapiere für Hundebetreuung
Zielgruppe
Mein Unternehmen richtet sich an Hundehalter, die freudig mit ihrem Hund arbeiten oder trainieren wollen oder eine positiv arbeitende Hundebetreuung oder Gassi-Gänger suchen. Hierbei liegt der Fokus auf Emotionen des Hundes, Emotionen des Hundehalters, Körpersprache und kleinschrittiges Training. Gemeinsames freudiges Training schafft Vertrauen und Bindung und ermöglicht Hund und Halter Freiraum. Ziel des Angebotes ist es, dass Hundehalter Verständnis für die Emotionen und Interessen des Hundes zu entwickeln und das für sich zu nutzen lernen, dem Hund das geben, was er in der jeweiligen Situation braucht und das ganze auf wissenschaftlich fundierter Basis.
Aufgabenstellung
Das Logo muss enthalten sein, ansonsten sind der Kreativität keine Grenzen gesetzt :)
Es sollte nur von Rechnung, über Angebot für alles nutzbar sein.
Das Unternehmen ist ein Einzelunternehmen, sprich der Firmenname ist mein eigener Name 'Kerstin Wohlfahrt' und Wiesentrupp nur Website und Marke.

```html
<!DOCTYPE html>
<html lang="de">
<head>
<meta charset="utf-8">
<title>Wiesentrupp – Briefpapier</title>
<link href="https://fonts.googleapis.com/css2?family=Poppins:wght@400;500;600;700&display=swap" rel="stylesheet">
<style>
  :root{
    --green:#8bb829;
    --slate:#41575c;
    --text:#3d4c51;
    --paper:#ffffff;
    --backdrop:#dcdcdc;
  }
  *{box-sizing:border-box;margin:0;padding:0}
  html,body{width:1200px;height:898px;overflow:hidden;background:var(--backdrop);font-family:"Poppins",sans-serif;color:var(--text)}
  .letterhead{position:absolute;left:296px;top:19px;width:608px;height:860px;background:var(--paper);overflow:hidden;box-shadow:0 4px 18px rgba(0,0,0,.12)}
  .header-wave{position:absolute;left:0;top:0;width:608px;height:120px}
  .footer-wave{position:absolute;left:0;bottom:0;width:608px;height:170px}
  .site-url{position:absolute;left:56px;top:52px;color:#fff;font-weight:600;font-size:9px;letter-spacing:.2px}
  .brand-name{position:absolute;right:60px;top:66px;font-weight:600;font-size:30px;color:var(--slate);letter-spacing:-.5px}
  .sender-line{position:absolute;left:70px;top:170px;font-size:6.5px;color:var(--green);font-weight:500}
  .sender-line strong{font-weight:600}
  .recipient{position:absolute;left:70px;top:186px;font-size:9px;line-height:12.5px;font-style:normal}
  .recipient strong{font-weight:600}
  .date{position:absolute;right:70px;top:250px;font-size:8.5px}
  .subject{position:absolute;left:70px;top:312px;font-size:11.5px;font-weight:600;color:var(--slate)}
  .body{position:absolute;left:70px;top:338px;width:470px;font-size:8.6px;line-height:12.6px}
  .body p{margin-bottom:12.6px}
  .closing{position:absolute;left:70px;top:575px;font-size:8.6px;line-height:12.6px}
  .footer-info{position:absolute;left:0;bottom:0;width:608px;height:110px;color:#fff;font-size:6.6px;line-height:9.5px;z-index:1}
  .footer-company{position:absolute;left:60px;top:76px;color:var(--green);font-weight:600;font-size:9.5px}
  .footer-address{position:absolute;left:200px;top:64px}
  .footer-contact{position:absolute;left:320px;top:40px}
  .footer-contact li{list-style:none;display:flex;align-items:center;gap:4px}
  .footer-contact svg{width:6px;height:6px;flex:none}
  .footer-bank{position:absolute;left:455px;top:18px}
  .footer-bank .label{color:var(--green);font-weight:600}
  .footer-bank dl{display:grid;grid-template-columns:30px auto}
  .footer-bank dt{font-weight:600}
  .strong{font-weight:600}
</style>
</head>
<body>
<main class="letterhead">
  <svg class="header-wave" viewBox="0 0 608 120" aria-hidden="true">
    <path d="M0 0H608V22C520 22 440 40 360 70C260 108 120 110 0 102Z" fill="var(--green)"/>
    <path d="M505 42C545 31 585 28 608 29V47C585 40 545 38 505 42Z" fill="var(--slate)"/>
  </svg>
  <div class="site-url">www.wiesentrupp.de</div>
  <div class="brand-name">Wiesentrupp</div>

  <div class="sender-line"><strong>Wiesentrupp GmbH</strong> &nbsp;|&nbsp; Musterstraße 1 &nbsp;|&nbsp; 12345 Musterstadt</div>
  <address class="recipient">
    <strong>Musterfirma GmbH</strong><br>Max Mustermann<br>Musterstraße 123<br>12345 Musterstadt
  </address>
  <div class="date">Musterstadt, 01.01.2022</div>

  <h1 class="subject">Betreff: Endam, omni dolor sam asperro que eos es</h1>
  <section class="body">
    <p>Uptassi quo volupta dit aliberis dolutas pelestrum sendi remquam repellent as autemodis etu­rit faciae illorrorest, omnimilit, qui ut endiscillam quid que sandero eiunt eror rest quam, tem­porunt officip sandam imi, sit acepudandis cor si cus, cum adios nonsedipsa consequ aesedit rem. Minus, inis am nos nossus vendaer uptiis mi, quiae con possi natis etur, simagna tionsed ullo venditia id ut auda isqui occus.</p>
    <p>Porest ma dolupta et accusdamusam sunt omnimil laborestia con commolum fugiaerio et iunt labor sequi velite et desciis sero modis nullandes del molliquo iliquis et eaquaspere sitiis es ele­nis dolendant exceperes es elenis dolendant exceperes es everest ibeatentia voloris ad millate il inctur? eatentia voloris ad millate il inctur? Qui vent venti ilibus.</p>
    <p>Excessi vel maximpo rporepe poreperum qui omniste eatenda quo es et omniaepudam, qui debissinci ullabor eptatempor modiorrum quos sus dolum ad quos et quias alissi debis nullore strunt porerum, sit vole.</p>
  </section>
  <div class="closing">Herzlichst,<br>Erika Mustermann</div>

  <svg class="footer-wave" viewBox="0 0 608 170" aria-hidden="true">
    <path d="M0 96C45 100 85 101 125 99C85 106 45 107 0 107Z" fill="var(--green)"/>
    <path d="M0 114C100 130 200 118 300 90C400 62 500 40 608 30V170H0Z" fill="var(--slate)"/>
  </svg>
  <footer class="footer-info">
    <div class="footer-company">Wiesentrupp GmbH</div>
    <div class="footer-address">Musterstraße 1<br>12345 Musterstadt<br><span class="strong">Geschäftsführung:</span><br>Erika Mustermann</div>
    <ul class="footer-contact">
      <li><svg viewBox="0 0 10 10"><path d="M2 0L4 2.5 3 4Q4 6 6 7L7.5 6 10 8 8.5 10Q1 9 0 1.5Z" fill="var(--green)"/></svg>+49 (0)1234 – 123 456 78</li>
      <li><svg viewBox="0 0 10 10"><rect x="2.5" y="0" width="5" height="10" rx="1" fill="none" stroke="var(--green)" stroke-width="1.2"/></svg>+49 (0)1234 – 123 456 78</li>
      <li><svg viewBox="0 0 10 10"><rect x="0" y="2" width="10" height="6.5" fill="var(--green)"/><path d="M0 2L5 6 10 2" fill="none" stroke="var(--slate)" stroke-width="1"/></svg>kontakt@wiesentrupp.de</li>
      <li class="strong">www.wiesentrupp.de</li>
    </ul>
    <div class="footer-bank">
      <div class="label">Bankverbindung</div>
      <div class="strong">Musterbank AG</div>
      <dl><dt>IBAN:</dt><dd>DE12 1234 1234 1234 1234 00</dd><dt>BIC:</dt><dd>ABCDEFGHJK</dd></dl>
    </div>
  </footer>
</main>
</body>
</html>
```